Brindale transport business cards

Front of card, Looking for my logo on one side of the card

Back of card,
Brindale Transport Maintenance
Onsite Cars, Trucks & trailer maintenance and repairs
Ronan Brindale
0452819036
Brindaletm@fernmail.com

```html
<!DOCTYPE html>
<html lang="en">
<head>
<meta charset="utf-8">
<title>Brindale Transport Maintenance – Business Cards</title>
<link rel="stylesheet" href="https://fonts.googleapis.com/css2?family=Montserrat:wght@400;500;800;900&display=swap">
<style>
  :root {
    --page: #1c1c1d;
    --card: #2b2b2d;
    --blue: #1a74e0;
    --blue-deep: #0d3f8f;
    --blue-bright: #2b8cf0;
    --silver: #c9ccd1;
    --white: #ffffff;
  }
  * { box-sizing: border-box; margin: 0; padding: 0; }
  html, body {
    width: 1200px; height: 900px; overflow: hidden;
    background: var(--page);
    font-family: "Montserrat", sans-serif;
  }
  .card {
    position: absolute; left: 250px; width: 700px; height: 400px;
    background: var(--card); border-radius: 18px; overflow: hidden;
    box-shadow: 0 10px 30px rgba(0,0,0,.5);
  }
  .card--front { top: 40px; }
  .card--back { top: 460px; }

  /* front */
  .front-photo {
    position: absolute; left: 180px; top: 0; width: 400px; height: 340px;
    background: radial-gradient(ellipse at 50% 40%, rgba(40,70,120,.35), rgba(43,43,45,0) 70%);
  }
  .front-band {
    position: absolute; left: 0; bottom: 0; width: 100%; height: 44px;
    background: linear-gradient(180deg, var(--blue-bright), var(--blue-deep));
    border-top: 4px solid var(--silver);
  }
  .brand { position: absolute; display: flex; align-items: center; gap: 18px; }
  .brand__mark { background: var(--blue); flex: none; }
  .brand__name {
    color: var(--white); font-weight: 800; text-transform: uppercase; line-height: 1.05;
  }
  .brand__name span { display: block; }
  .card--front .brand { left: 150px; top: 130px; }
  .card--front .brand__mark { width: 60px; height: 60px; }
  .card--front .brand__name { font-size: 56px; }
  .card--front .brand__name span + span { font-size: 24px; letter-spacing: 2px; }

  /* back */
  .card--back .brand { left: 210px; top: 45px; gap: 14px; }
  .card--back .brand__mark { width: 44px; height: 44px; }
  .card--back .brand__name { font-size: 40px; }
  .card--back .brand__name span + span { font-size: 17px; letter-spacing: 1.5px; }

  .holder {
    position: absolute; left: 40px; top: 178px;
    color: var(--blue); font-weight: 900; font-size: 29px; letter-spacing: 1px;
    text-transform: uppercase; white-space: nowrap;
  }
  .divider {
    position: absolute; left: 352px; top: 162px; width: 2px; height: 70px; background: var(--blue);
  }
  .contacts { position: absolute; left: 370px; top: 162px; list-style: none; }
  .contacts li {
    display: flex; align-items: center; gap: 10px; white-space: nowrap;
    color: var(--white); font-size: 17px; font-weight: 500; height: 35px;
  }
  .contacts svg { width: 16px; height: 16px; fill: var(--blue); flex: none; }

  .swoosh { position: absolute; left: 0; top: 0; width: 700px; height: 400px; }
  .swoosh text { fill: var(--white); font-family: "Montserrat", sans-serif; font-weight: 500; }
</style>
</head>
<body>

<section class="card card--front" aria-label="Card front">
  <div class="front-photo" role="img" aria-label="Faint background photo of a truck cab"></div>
  <div class="brand">
    <div class="brand__mark"></div>
    <p class="brand__name"><span>Brindale</span><span>Transport Maintenance</span></p>
  </div>
  <div class="front-band"></div>
</section>

<section class="card card--back" aria-label="Card back">
  <svg class="swoosh" viewBox="0 0 700 400" aria-hidden="true">
    <defs>
      <linearGradient id="swoosh-fill" x1="0" y1="1" x2="1" y2="0">
        <stop offset="0" stop-color="#1a74e0"/>
        <stop offset="1" stop-color="#0d3f8f"/>
      </linearGradient>
    </defs>
    <path d="M0 345 C300 335 520 300 700 230 L700 400 L0 400 Z" fill="url(#swoosh-fill)"/>
    <path d="M0 345 C300 335 520 300 700 230" fill="none" stroke="#c9ccd1" stroke-width="5"/>
    <text x="300" y="358" font-size="16" transform="rotate(-8 300 358)">Brindale Transport Maintenance</text>
    <text x="235" y="388" font-size="15" transform="rotate(-8 235 388)">Onsite Cars, Trucks &amp; trailer maintenance and repairs</text>
  </svg>

  <div class="brand">
    <div class="brand__mark"></div>
    <p class="brand__name"><span>Brindale</span><span>Transport Maintenance</span></p>
  </div>

  <p class="holder">Ronan Brindale</p>
  <div class="divider"></div>
  <ul class="contacts">
    <li>
      <svg viewBox="0 0 24 24" aria-hidden="true"><path d="M6.6 10.8a15 15 0 0 0 6.6 6.6l2.2-2.2c.3-.3.7-.4 1-.2 1.1.4 2.3.6 3.6.6.6 0 1 .4 1 1V20c0 .6-.4 1-1 1A17 17 0 0 1 3 4c0-.6.4-1 1-1h3.5c.6 0 1 .4 1 1 0 1.3.2 2.5.6 3.6.1.3 0 .7-.2 1z"/></svg>
      0452819036
    </li>
    <li>
      <svg viewBox="0 0 24 24" aria-hidden="true"><path d="M2 5h20v14H2z M3 6l9 7 9-7" stroke="#2b2b2d" stroke-width="1.5"/></svg>
      Brindaletm@fernmail.com
    </li>
  </ul>
</section>

</body>
</html>
```